Minimalist theatrical poster for the film

Create a poster, using some of the attached images for inspiration. Please match the font of the teaser poster for the title (The Bluewater) and leave space at the bottom for the credits block, which I will add later. Any characters presented on the poster should resemble the actors in the film, and not be clip art. The movie is about Owen, a 14 year old in the summer of 2001, and his first love (Greta). As he falls for her, he lets himself still be distracted by his good friend Maisie, eventually causing trouble in his relationships with Greta, Maisie, and best friend Theo. Trailer is included in the files below! Extra credit for a good marketing tag along the lines of "remember your first love" or something about the film being a romantic comedy adventure etc.

```html
<!DOCTYPE html>
<html lang="en">
<head>
<meta charset="utf-8">
<title>Owen &amp; The Bluewater — Poster</title>
<link rel="stylesheet" href="https://fonts.googleapis.com/css2?family=Kaushan+Script&family=Oswald:wght@500&display=swap">
<style>
  :root {
    --backdrop: #1f1f1f;
    --ink: #ffffff;
    --credit-ink: #111111;
    --night: #0d0a1e;
    --indigo: #2a1f66;
    --violet: #5a2f86;
    --amber: #f2c23a;
    --gold: #fff08a;
    --mauve: #c06a9a;
    --rose: #e8a3c0;
    --cream: #fff1e6;
  }
  * { margin: 0; padding: 0; box-sizing: border-box; }
  html, body {
    width: 1004px; height: 1200px; overflow: hidden;
    background: var(--backdrop);
  }
  .poster {
    position: absolute; left: 148px; top: 100px;
    width: 707px; height: 1000px; overflow: hidden;
    box-shadow: 0 12px 28px rgba(0,0,0,.6);
  }
  .poster-photo {
    position: absolute; inset: 0;
    background:
      radial-gradient(ellipse 200px 130px at 330px 330px, var(--gold) 0%, rgba(242,194,58,.75) 45%, rgba(242,194,58,0) 100%),
      radial-gradient(ellipse 340px 220px at 300px 300px, rgba(200,150,60,.8) 0%, rgba(120,70,90,.4) 60%, rgba(40,25,70,0) 100%),
      radial-gradient(ellipse 220px 260px at 600px 800px, var(--cream) 0%, rgba(240,190,200,.6) 45%, rgba(230,160,190,0) 100%),
      linear-gradient(180deg, var(--night) 0%, #1d1636 14%, #3a2a4a 30%, var(--indigo) 46%, var(--violet) 56%, var(--mauve) 68%, var(--rose) 82%, #b56a9c 100%);
  }
  .title {
    position: absolute; color: var(--ink);
    font-family: "Kaushan Script", cursive;
    line-height: 1; white-space: nowrap;
  }
  .title-name { left: 72px; top: 398px; font-size: 84px; }
  .title-amp  { left: 188px; top: 492px; font-size: 42px; }
  .title-the  { left: 126px; top: 546px; font-size: 50px; }
  .title-word { left: 216px; top: 528px; font-size: 88px; }
  .credits {
    position: absolute; left: 0; right: 0; top: 868px;
    font-family: "Oswald", sans-serif; font-weight: 500;
    color: var(--credit-ink); text-transform: uppercase;
    text-align: center; line-height: 1;
  }
  .credit-line { font-size: 15px; margin-bottom: 8px; white-space: nowrap; letter-spacing: -.2px; }
  .credit-line small { font-size: 6px; display: inline-block; vertical-align: middle; line-height: 1; margin: 0 2px; }
</style>
</head>
<body>
  <div class="poster">
    <div class="poster-photo" role="img" aria-label="Dreamy photo: a teenage boy and girl holding hands on park swings in golden summer light, above a soft-focus close-up of the pair kissing in purple and pink tones"></div>

    <div class="title title-name">Owen</div>
    <div class="title title-amp">&amp;</div>
    <div class="title title-the">The</div>
    <div class="title title-word">Bluewater</div>

    <div class="credits">
      <p class="credit-line">Studio Name Pictures <small>presents a</small> Producers <small>a film by</small> Script Writer Actor One Actor Two “Movie Title”</p>
      <p class="credit-line"><small>music<br>by</small>The Musician <small>costume<br>designer</small>Designer Name <small>edited<br>by</small>Editors Name <small>production<br>designer</small> Designers Name <small>director of<br>photography</small> Cinematographer</p>
      <p class="credit-line"><small>executive<br>producer</small> Ex Producer 1 Ex Producer 2 <small>produced<br>by</small> Producer One Producer 2 <small>story<br>by</small> Story Writer</p>
      <p class="credit-line"><small>screenplay<br>by</small> Screen Writer <small>directed<br>by</small> Director Name</p>
    </div>
  </div>
</body>
</html>
```